Change the world and help build SpinLOOM.tv!

We need a mobile website design for our Beta release - see wireframes attached.
See our Logo design files attached along with fonts, etc.
Please see enclosed .PDF that provides a great overview of our company, LOOM.
Any questions, feel free to ask - we're very engaged here on Sketch Hive and will make ourselves available.
Thanks!
Tobias
Updates
Very pleased with what's coming in! Would like to see some more variety and more volume of designs.
Target Market(s)
Ages 13+ (all genders, races, creeds, income levels, etc)
Coding
Coded - Design and coding required
Number of Pages Required
5+ page
Font styles to use
Colors
Designer to choose colors to be used in the design.
Look and feel
Each slider illustrates characteristics of the customer's brand and the style your logo design should communicate.

```html
<!DOCTYPE html>
<html lang="en">
<head>
<meta charset="utf-8">
<title>SpinLOOM.tv – Beta Pages</title>
<link href="https://fonts.googleapis.com/css2?family=Lato:wght@400;700;900&display=swap" rel="stylesheet">
<style>
:root{
  --navy:#26355f;
  --navy-deep:#1d2a4d;
  --sky:#5db7de;
  --paper:#ffffff;
  --mist:#eef0f4;
  --line:#cfd4de;
  --ink:#2a2f3d;
  --muted:#6b7284;
  --stage:#e9ebef;
}
*{box-sizing:border-box;margin:0;padding:0}
html,body{width:1200px;height:3600px;overflow:hidden}
body{background:var(--stage);font-family:'Lato',sans-serif;color:var(--ink)}
.pages{display:flex;flex-direction:column;gap:25px;width:1200px;height:3600px}
.page{position:relative;width:1200px;height:700px;background:var(--paper);overflow:hidden;display:flex;flex-direction:column}

.site-header{height:70px;display:flex;align-items:center;justify-content:space-between;padding:0 60px;background:var(--paper);position:relative;z-index:2}
.brand{display:flex;align-items:center;gap:10px;color:var(--navy);font-weight:900;font-size:24px}
.brand-mark{width:22px;height:22px;background:var(--navy)}
.nav-actions{display:flex;gap:14px}
.btn{display:inline-block;font-family:'Lato',sans-serif;font-weight:700;font-size:13px;padding:9px 26px;border-radius:20px;color:#fff;border:0}
.btn-join{background:var(--sky)}
.btn-artist{background:var(--navy)}

.site-footer{height:50px;display:flex;align-items:center;justify-content:center;gap:18px;font-size:12px;color:var(--muted);background:var(--paper);position:relative;z-index:2;margin-top:auto}
.site-footer a{color:var(--muted);text-decoration:none}
.site-footer a.active{color:var(--sky)}
.site-footer .sep{color:var(--line)}

/* home */
.hero{position:relative;flex:1;margin:0 40px;display:flex;flex-direction:column;align-items:center;justify-content:center}
.hero-photo{position:absolute;inset:0;background:linear-gradient(180deg,#9aa4b4 0%,#6e7688 45%,#3d4661 100%)}
.hero-title{position:relative;color:#fff;font-weight:900;font-size:34px;letter-spacing:1px;text-transform:uppercase;text-align:center;margin-top:40px}
.hero-cta{position:relative;margin-top:auto;margin-bottom:40px;background:var(--navy);color:#fff;font-weight:700;font-size:13px;letter-spacing:1px;padding:12px 36px;border-radius:24px;border:2px solid #fff}

/* form pages */
.band{position:absolute;left:0;right:0;bottom:50px;height:330px;background:var(--navy)}
.card{position:relative;z-index:1;width:560px;margin:10px auto 0;background:var(--paper);border:1px solid var(--line);padding:22px 40px 24px;box-shadow:0 4px 16px rgba(0,0,0,.12)}
.intro{text-align:center;margin:6px auto 10px;width:620px;position:relative;z-index:1}
.intro h1{font-size:22px;font-weight:900;color:var(--navy);line-height:1.3}
.intro p{font-size:12px;color:var(--muted);margin-top:6px;line-height:1.5}
.field{display:flex;align-items:center;margin-bottom:8px}
.field label{width:130px;font-size:12px;color:var(--muted);text-align:right;padding-right:14px}
.field .input{flex:1;height:26px;border:1px solid var(--line);background:var(--mist)}
.field.tall{align-items:flex-start}
.field.tall .input{height:80px;font-size:11px;color:var(--muted);padding:6px 8px}
.submit{display:block;margin:14px auto 0;background:var(--sky);color:#fff;font-weight:700;font-size:13px;padding:9px 40px;border-radius:20px;width:max-content}

/* thank you */
.thanks{position:relative;z-index:1;width:600px;margin:40px auto 0;background:var(--paper);border:1px solid var(--line);padding:40px 50px;text-align:center;box-shadow:0 4px 16px rgba(0,0,0,.12)}
.thanks .brand{justify-content:center;font-size:30px}
.thanks .brand-mark{width:26px;height:26px}
.thanks h1{font-size:34px;font-weight:900;color:var(--navy);margin:28px 0 18px}
.thanks p{font-size:14px;color:var(--muted);line-height:1.6;margin-bottom:12px}
.thanks .sign{color:var(--navy);font-weight:700;margin-top:18px}
</style>
</head>
<body>
<main class="pages">

  <!-- Home -->
  <section class="page page-home">
    <header class="site-header">
      <div class="brand"><span class="brand-mark"></span>SpinLOOM.tv</div>
      <nav class="nav-actions"><span class="btn btn-join">Join Beta</span><span class="btn btn-artist">Artist Sign Up</span></nav>
    </header>
    <div class="hero">
      <div class="hero-photo" role="img" aria-label="Photo of a diverse, smiling crowd of people of all ages"></div>
      <h1 class="hero-title">Join the movement. Help shape LOOM.</h1>
      <span class="hero-cta">SUPPORT OUR FUNDSPARK CAMPAIGN</span>
    </div>
    <footer class="site-footer">
      <a class="active">Terms and Conditions</a><span class="sep">|</span><a>Privacy Policy</a><span class="sep">|</span><a>About LOOM</a><span class="sep">|</span><a>The LOOM Team</a>
    </footer>
  </section>

  <!-- Join Beta -->
  <section class="page page-beta">
    <header class="site-header">
      <div class="brand"><span class="brand-mark"></span>SpinLOOM.tv</div>
      <nav class="nav-actions"><span class="btn btn-join">Join Beta</span><span class="btn btn-artist">Artist Sign Up</span></nav>
    </header>
    <div class="band"></div>
    <div class="intro">
      <h1>"Sign up to receive an invitation to join our pre-launch (Beta) version of LOOM!</h1>
      <p>Join our community of hopeful SpinLOOM.tv users and help build something great for millions of people!</p>
    </div>
    <form class="card">
      <div class="field"><label>Name</label><span class="input"></span></div>
      <div class="field"><label>Date of Birth</label><span class="input"></span></div>
      <div class="field"><label>Address</label><span class="input"></span></div>
      <div class="field"><label>Email</label><span class="input"></span></div>
      <div class="field"><label>Phone</label><span class="input"></span></div>
      <div class="field tall"><label>Make your voice be heard</label><span class="input"></span></div>
      <span class="submit">Sign Up</span>
    </form>
    <footer class="site-footer">
      <a class="active">Terms and Conditions</a><span class="sep">|</span><a>Privacy Policy</a><span class="sep">|</span><a>About LOOM</a><span class="sep">|</span><a>The LOOM Team</a>
    </footer>
  </section>

  <!-- Beta thank you -->
  <section class="page page-beta-thanks">
    <header class="site-header">
      <div class="brand"><span class="brand-mark"></span>SpinLOOM.tv</div>
      <nav class="nav-actions"><span class="btn btn-join">Join Beta</span><span class="btn btn-artist">Artist Sign Up</span></nav>
    </header>
    <div class="band"></div>
    <article class="thanks">
      <div class="brand"><span class="brand-mark"></span>SpinLOOM.tv</div>
      <h1>"Thank You For Signing Up!</h1>
      <p>Please check your email for more details about our Beta program. We will reach out soon with your invite.</p>
      <p>We're so excited to have you on board. You're helping shape the future of entertainment.</p>
      <p class="sign">With love,<br>SpinLOOM.tv team</p>
    </article>
    <footer class="site-footer">
      <a class="active">Terms and Conditions</a><span class="sep">|</span><a>Privacy Policy</a><span class="sep">|</span><a>About LOOM</a><span class="sep">|</span><a>The LOOM Team</a>
    </footer>
  </section>

  <!-- Artist sign up -->
  <section class="page page-artist">
    <header class="site-header">
      <div class="brand"><span class="brand-mark"></span>SpinLOOM.tv</div>
      <nav class="nav-actions"><span class="btn btn-join">Join Beta</span><span class="btn btn-artist">Artist Sign Up</span></nav>
    </header>
    <div class="band"></div>
    <div class="intro">
      <h1>"Join LOOM's Artist Program!</h1>
      <p>It's time to help creators everywhere get the fair share they deserve. Join our Artist Program today.<br>Please tell us a bit about your work and we'll be in touch.<br>With love, SpinLOOM.tv team</p>
    </div>
    <form class="card">
      <div class="field"><label>Name</label><span class="input"></span></div>
      <div class="field"><label>Date of Birth</label><span class="input"></span></div>
      <div class="field"><label>Address</label><span class="input"></span></div>
      <div class="field"><label>Email</label><span class="input"></span></div>
      <div class="field"><label>Phone</label><span class="input"></span></div>
      <div class="field"><label>Link to portfolio</label><span class="input"></span></div>
      <div class="field tall"><label>About you</label><span class="input">Tell us about yourself</span></div>
      <span class="submit">Sign Up</span>
    </form>
    <footer class="site-footer">
      <a class="active">Terms and Conditions</a><span class="sep">|</span><a>Privacy Policy</a><span class="sep">|</span><a>About LOOM</a><span class="sep">|</span><a>The LOOM Team</a>
    </footer>
  </section>

  <!-- Artist thank you -->
  <section class="page page-artist-thanks">
    <header class="site-header">
      <div class="brand"><span class="brand-mark"></span>SpinLOOM.tv</div>
      <nav class="nav-actions"><span class="btn btn-join">Join Beta</span><span class="btn btn-artist">Artist Sign Up</span></nav>
    </header>
    <div class="band"></div>
    <article class="thanks">
      <div class="brand"><span class="brand-mark"></span>SpinLOOM.tv</div>
      <h1>"Thank You For Your Interest!</h1>
      <p>Please check your email for more details about our Artist Program. We can't wait to see what you create.</p>
      <p class="sign">With love,<br>SpinLOOM.tv team</p>
    </article>
    <footer class="site-footer">
      <a class="active">Terms and Conditions</a><span class="sep">|</span><a>Privacy Policy</a><span class="sep">|</span><a>About LOOM</a><span class="sep">|</span><a>The LOOM Team</a>
    </footer>
  </section>

</main>
</body>
</html>
```